Sustainably Transforming Education

Company is education services based. early learning through adult and corporate. Focus is national government policy and program design and delivery alongside a research based and academically grounded set of approaches to planning, evaluation, and change management.I am looking for an innovative design position that aligns with the global agendas for innovation, creativity and collaboration at international and national policy levels (velmora is a name that reflects these qualities - colours need to reflect amythyst in some way). I also need a design that translates from a business card as 1 medium of interaction to a template that can work in word/powerpoint etc to support both stationery as well as a digital strategy across multiple channels (fb/twit/etc)There is no slogan/tag line for the company and their is no logo. I was looking to just leverage the name - have currently played around with various fonts (ending up with cuisine - all lowercase).

Industry/Entity Type

Adult

Contact Information for Business Card

name: velmora (all lowercase)Chairman: Andrew CrowMobile: +61 418 902 131Web: www.velmora.comemail: martin.hessel@velmora.com

Font styles to use
Script
Other font styles liked:
• cuisine

Colors
e34298
e667a6
33a6d7
aaaaaa

Requirements
Nice to have
• https://www.filecrate.net/sh/kx7trwq2pzn4lme/BBQfinaRtYe0wplHJzcVnNuQo?dl=0
• Link to the printhollow templates used to begin this process....the one with the lines was about people intersecting (collaborating).....the organic shapes one more of a fluid feel of people coming together - the overall shape being largely spherical could represent a "global" feel.....anyway that is how I was thinking about these

```html
<!DOCTYPE html>
<html lang="en">
<head>
<meta charset="utf-8">
<title>velmora — Business Card</title>
<link rel="stylesheet" href="https://fonts.googleapis.com/css2?family=Kaushan+Script&display=swap">
<style>
  :root {
    --amethyst: #e34298;
    --amethyst-soft: #e667a6;
    --ink-black: #15181b;
    --paper-white: #ffffff;
    --map-grey: #aaaaaa;
    --script: "Kaushan Script", cursive;
  }
  html, body {
    margin: 0;
    padding: 0;
    width: 1200px;
    height: 740px;
    overflow: hidden;
    background: var(--paper-white);
  }
  .card {
    position: relative;
    width: 1200px;
    height: 740px;
    overflow: hidden;
    font-family: var(--script);
  }
  .card__artwork {
    position: absolute;
    inset: 0;
    width: 1200px;
    height: 740px;
  }
  .holder-name {
    position: absolute;
    left: 328px;
    top: 92px;
    margin: 0;
    font-size: 68px;
    font-weight: 400;
    line-height: 1;
    color: var(--amethyst);
    white-space: nowrap;
  }
  .holder-role {
    position: absolute;
    left: 326px;
    top: 170px;
    margin: 0;
    font-size: 52px;
    font-weight: 400;
    line-height: 1;
    color: var(--ink-black);
  }
  .title-rule {
    position: absolute;
    left: 326px;
    top: 228px;
    width: 730px;
    height: 3px;
    background: var(--amethyst);
  }
  .contact-list {
    position: absolute;
    left: 620px;
    top: 318px;
    margin: 0;
    padding: 0;
    list-style: none;
  }
  .contact-list__item {
    display: flex;
    align-items: center;
    height: 44px;
    font-size: 40px;
    line-height: 1;
    color: var(--ink-black);
    white-space: nowrap;
  }
  .contact-list__icon {
    width: 30px;
    height: 30px;
    flex: none;
    margin-right: 28px;
  }
  .contact-list__item--phone .contact-list__icon { margin-right: 22px; }
  .brand-name {
    position: absolute;
    left: 104px;
    top: 552px;
    margin: 0;
    font-size: 84px;
    font-weight: 400;
    line-height: 1;
    color: var(--paper-white);
  }
</style>
</head>
<body>
<main class="card">
  <svg class="card__artwork" viewBox="0 0 1000 617" preserveAspectRatio="none">
    <defs>
      <clipPath id="centre-panel-clip">
        <path d="M150,0 L760,0 C880,80 965,260 990,505 C800,480 570,445 430,392 C300,340 205,190 150,0 Z"/>
      </clipPath>
      <radialGradient id="map-wash" cx="50%" cy="50%" r="60%">
        <stop offset="0%" stop-color="var(--map-grey)" stop-opacity="0.14"/>
        <stop offset="100%" stop-color="var(--map-grey)" stop-opacity="0.04"/>
      </radialGradient>
    </defs>

    <rect class="band-dark" width="1000" height="617" fill="var(--ink-black)"/>

    <path class="stripe-light" d="M0,0 L62,0 C130,250 300,420 560,500 C700,545 780,590 830,617 L0,617 Z" fill="var(--paper-white)"/>

    <path class="field-amethyst" d="M0,0 L42,0 C110,260 290,430 540,515 C660,555 720,590 760,617 L0,617 Z" fill="var(--amethyst)"/>

    <path class="panel-centre" d="M150,0 L760,0 C880,80 965,260 990,505 C800,480 570,445 430,392 C300,340 205,190 150,0 Z" fill="var(--paper-white)"/>

    <g clip-path="url(#centre-panel-clip)">
      <rect class="map-area" role="img" aria-label="Faint grey world map in the background" x="300" y="50" width="620" height="400" rx="180" fill="url(#map-wash)"/>
    </g>

    <path class="swoosh-top" d="M345,12 C390,-8 560,-2 700,18 C785,38 835,80 860,125 C790,78 705,56 600,48 C500,42 405,38 345,12 Z" fill="var(--amethyst-soft)"/>

    <path class="swoosh-right" d="M815,112 C905,150 975,250 1000,330 L1000,500 L985,500 C965,310 905,195 815,112 Z" fill="var(--amethyst)"/>
  </svg>

  <h1 class="holder-name">Martin Hessel</h1>
  <p class="holder-role">Chairman</p>
  <div class="title-rule"></div>

  <ul class="contact-list">
    <li class="contact-list__item contact-list__item--phone">
      <svg class="contact-list__icon" viewBox="0 0 30 30" aria-hidden="true">
        <path d="M3,11 C3,6 27,6 27,11 L27,13 L21,13 L21,10 L9,10 L9,13 L3,13 Z" fill="var(--amethyst)"/>
        <path d="M9,14 L21,14 L26,25 L4,25 Z" fill="var(--amethyst)"/>
        <g fill="var(--paper-white)">
          <circle cx="12" cy="18" r="1.2"/><circle cx="15" cy="18" r="1.2"/><circle cx="18" cy="18" r="1.2"/>
          <circle cx="11" cy="21.5" r="1.2"/><circle cx="15" cy="21.5" r="1.2"/><circle cx="19" cy="21.5" r="1.2"/>
        </g>
      </svg>
      <span>+61 437 615 284</span>
    </li>
    <li class="contact-list__item contact-list__item--email">
      <svg class="contact-list__icon" viewBox="0 0 30 30" aria-hidden="true">
        <rect x="2" y="5" width="26" height="20" fill="var(--amethyst)"/>
        <path d="M4,8 L15,17 L26,8 M4,23 L12,15 M26,23 L18,15" fill="none" stroke="var(--paper-white)" stroke-width="1.6"/>
      </svg>
      <span>martin.hessel@velmora.com</span>
    </li>
    <li class="contact-list__item contact-list__item--web">
      <svg class="contact-list__icon" viewBox="0 0 30 30" aria-hidden="true">
        <circle cx="15" cy="15" r="12" fill="var(--amethyst)"/>
        <g fill="none" stroke="var(--paper-white)" stroke-width="1.4">
          <ellipse cx="15" cy="15" rx="5" ry="12"/>
          <line x1="15" y1="3" x2="15" y2="27"/>
          <line x1="3" y1="15" x2="27" y2="15"/>
          <path d="M5,9 L25,9 M5,21 L25,21"/>
        </g>
      </svg>
      <span>www.velmora.com</span>
    </li>
  </ul>

  <p class="brand-name">velmora</p>
</main>
</body>
</html>
```